Flyer for Medical practice welcoming new patients

We need a DL size brochure designed for Medical practice to advertise that we are accepting new patients. Our practice has special interests in women's and children's health and seniors health. Our existing advertising materials are in the colour scheme of purples I have uploaded our logo which includes our colour scheme.

Target Market(s)

Versatile to target anyone looking for a small medical practice that offers continuous care of seeing the same Doctor every time

Industry/Entity Type

Advertising

Font styles to use
Serif

Colors
6b449b
876aae
b7a5cc

Requirements
Must have
• The practice logo of just the picture not Dr Marla Thorncroft.
• Purple colour scheme.
• Practice name: Larkhaven Medical Practice.
• Address: 147 Tremont Rd, Larkhaven NSW 2500.
• Phone: 4873 6159.
• DL size brochure
• Welcoming new patients ( a strong emphasis needs to be placed on this)
• Nurse and onsite ECG's and lung function tests.
• Travel vaccines including yellow fever
• Bulk billing for tertiary students
• We would also like design to alter the text so that we can change the points to be reflect who we are targeting at the time.
Nice to have
• The practice logo with Dr Marla Thorncroft somewhere not as a feature as the practice no longer goes under this name but is still well known as Dr Thorncroft's.

```html
<!DOCTYPE html>
<html lang="en">
<head>
<meta charset="utf-8">
<title>Larkhaven Medical Practice – DL Flyer</title>
<link rel="stylesheet" href="https://fonts.googleapis.com/css2?family=Lato:wght@300;400&family=Oswald:wght@600&display=swap">
<style>
  :root {
    --purple-deep: #6b449b;
    --purple-mid: #876aae;
    --purple-soft: #b7a5cc;
    --purple-ink: #5a2d7a;
    --lavender-mist: #ece7f3;
    --panel-grey: #e6e6e6;
    --paper: #ffffff;
    --backdrop: #b9b9b9;
  }
  html, body {
    margin: 0;
    width: 1200px;
    height: 1000px;
    overflow: hidden;
    background: var(--backdrop);
  }
  .flyer {
    position: absolute;
    left: 347px;
    top: 30px;
    width: 440px;
    height: 922px;
    background: var(--paper);
    overflow: hidden;
    font-family: "Lato", sans-serif;
  }
  .flyer-artwork {
    position: absolute;
    inset: 0;
  }
  .brand-mark {
    position: absolute;
    left: 22px;
    top: 56px;
    width: 118px;
    height: 118px;
    border: 4px solid var(--purple-soft);
    border-radius: 50%;
    opacity: 0.6;
    box-sizing: border-box;
  }
  .practice-name {
    position: absolute;
    left: 8px;
    top: 182px;
    margin: 0;
    font-weight: 400;
    line-height: 1.15;
  }
  .practice-name .place {
    display: block;
    font-size: 26px;
    color: var(--purple-soft);
  }
  .practice-name .kind {
    display: block;
    font-size: 28px;
    color: var(--purple-ink);
  }
  .service-list {
    position: absolute;
    left: 8px;
    top: 378px;
    width: 350px;
    margin: 0;
    padding: 0;
    list-style: none;
    color: var(--purple-deep);
    font-size: 22px;
    line-height: 28px;
  }
  .service-list li {
    position: relative;
    padding-left: 16px;
  }
  .service-list li::before {
    content: "";
    position: absolute;
    left: 0;
    top: 11px;
    width: 11px;
    height: 11px;
    border-radius: 50%;
    background: var(--purple-deep);
  }
  .service-list li + li { margin-top: 28px; }
  .service-list li.tight { margin-top: 36px; line-height: 24px; }
  .contact {
    position: absolute;
    right: 10px;
    top: 826px;
    text-align: right;
    color: var(--purple-deep);
    font-size: 15px;
    line-height: 22px;
  }
  .contact-title {
    margin: 0 0 6px;
    font-family: "Oswald", sans-serif;
    font-weight: 600;
    font-size: 14px;
  }
  .contact p { margin: 0; }
  .contact svg { vertical-align: -3px; margin-right: 6px; }
  .contact .phone { margin-top: 4px; }
</style>
</head>
<body>
  <article class="flyer">
    <svg class="flyer-artwork" width="440" height="922" viewBox="0 0 440 922" aria-hidden="false">
      <defs>
        <linearGradient id="bandShade" x1="0" y1="0" x2="0" y2="1">
          <stop offset="0" stop-color="#876aae"/>
          <stop offset="1" stop-color="#6b449b"/>
        </linearGradient>
        <radialGradient id="mistFade" cx="0.5" cy="0.5" r="0.5">
          <stop offset="0" stop-color="#ece7f3" stop-opacity="0.95"/>
          <stop offset="1" stop-color="#ece7f3" stop-opacity="0"/>
        </radialGradient>
      </defs>
      <rect class="dotted-haze" role="img" aria-label="Soft lavender dotted texture behind the practice name" x="120" y="110" width="220" height="220" fill="url(#mistFade)"/>
      <rect class="dotted-haze" role="img" aria-label="Soft lavender dotted texture in the lower corner" x="220" y="560" width="260" height="380" fill="url(#mistFade)"/>
      <path class="purple-band" fill="url(#bandShade)"
        d="M148,0 L200,0 C215,90 300,210 440,230 L440,600
           C350,700 280,820 262,922 L152,922
           C190,800 300,650 335,500 C352,420 300,375 200,372
           C120,372 50,380 0,388 L0,322
           C120,298 240,276 330,268 C250,220 170,110 148,0 Z"/>
      <path class="grey-panel" fill="var(--panel-grey)" stroke="var(--paper)" stroke-width="14"
        d="M0,368 C150,356 340,350 388,420 C420,470 380,560 320,640
           C260,720 190,790 0,852 Z"/>
      <path class="grey-panel" fill="var(--panel-grey)" stroke="var(--paper)" stroke-width="14"
        d="M205,-10 L450,-10 L450,212 C360,218 268,150 228,80 C214,50 208,20 205,-10 Z"/>
    </svg>

    <div class="brand-mark" aria-hidden="true"></div>
    <h1 class="practice-name">
      <span class="place">Larkhaven</span>
      <span class="kind">Medical Practice</span>
    </h1>

    <ul class="service-list">
      <li>We are accepting new patients</li>
      <li>We have a nurse on site and can<br>&nbsp;do onsite ECG's and lung<br>function tests</li>
      <li class="tight">We offer travel vaccines<br>including yellow fever</li>
      <li class="tight">Bulk billing for tertiary<br>students</li>
    </ul>

    <address class="contact">
      <p class="contact-title">Contact Details:</p>
      <p><svg width="18" height="16" viewBox="0 0 18 16"><path d="M2,8 L9,2 L16,8 M4,7 V15 H14 V7" fill="none" stroke="#b7a5cc" stroke-width="1.6"/><rect x="7.5" y="10" width="3" height="5" fill="#b7a5cc"/></svg>147 Tremont Rd,</p>
      <p>Larkhaven NSW 2500.</p>
      <p class="phone"><svg width="14" height="16" viewBox="0 0 14 16"><rect x="0" y="0" width="14" height="16" rx="2" fill="#b7a5cc"/><path d="M5,3 C3,5 3,11 7,13 L8.5,11.5 L7,10 C6,9 6,7 6.5,6 L7.5,4.5 Z" fill="#fff"/></svg>4873 6159</p>
    </address>
  </article>
</body>
</html>
```